New E-Learning Website Design Wanted!

I am creating an E-learning website for those interested in getting certifications in the IT industry.
For example, courses related to VKT, Lomen, RJV certifications and national certifications in the IT industry in Japan will be offered.
You can think of sites such as Pindolia, Kestova, BrickSage, Minotell.
But I am targeting industries in Japan at the moment.
Also, I have uploaded screenshots of pages that I think are good.

The company is Velmont Data
I recently got my company logo designed so I attached pdf file to this project brief.
I would appreciate it if you can make the site match the color scheme of the logo.

Target Market(s)

I am targeting individuals as well as large IT companies in Japan

Industry/Entity Type

Education

Coding

Coded - Design and coding required

Number of Pages Required

4 page

Font styles to use
Sans Serif

Colors

Designer to choose colors to be used in the design.

Requirements
Must have
• One top page design
• One course page (https://tivokhub.example/courses/vkt-hosting-services)
• One learning page(where the learner can see the video)
• One blog page(https://info.tivokhub.example/resources?_ga=2.51827364.27461930.1629384756-830152947.1629384756)
Nice to have
• Pricing page

```html
<!DOCTYPE html>
<html lang="en">
<head>
<meta charset="utf-8">
<title>Velmont Data — IT Certification Courses</title>
<link rel="stylesheet" href="https://fonts.googleapis.com/css2?family=Lato:wght@400;700;900&family=Orbitron:wght@500;600&display=swap">
<style>
:root{
  --navy:#172a5e;
  --navy-dark:#0f1f4a;
  --teal:#1e9a9a;
  --ink:#1d2433;
  --text:#6b7280;
  --muted:#8a8f99;
  --line:#e3e5ea;
  --soft:#f2f2f3;
  --white:#ffffff;
  --sale:#b1202c;
}
*{margin:0;padding:0;box-sizing:border-box}
html,body{width:1200px;height:4728px;overflow:hidden}
body{font-family:'Lato',sans-serif;color:var(--ink);background:var(--white)}
.section{position:relative;width:1200px;overflow:hidden}
.abs{position:absolute}
.display{font-family:'Orbitron',sans-serif;font-weight:500;letter-spacing:1px}
.btn{position:absolute;display:flex;align-items:center;justify-content:center;gap:10px;font-weight:900;font-size:13px;text-transform:uppercase;letter-spacing:.2px;color:var(--white);background:var(--navy);border-radius:3px;text-decoration:none}
.btn .arrow{width:13px;height:13px}
.photo{position:absolute;border:4px solid var(--white);box-shadow:0 2px 10px rgba(0,0,0,.14)}

/* header */
.site-header{height:108px;border-bottom:1px solid var(--line)}
.logo{left:112px;top:36px;display:flex;align-items:center;gap:10px}
.logo-mark{width:28px;height:28px;background:var(--teal)}
.logo-name{font-size:21px;font-weight:700;color:var(--navy);letter-spacing:.3px}
.nav a{position:absolute;top:43px;font-size:14px;font-weight:700;color:var(--ink);text-decoration:none;transform:translateX(-50%);white-space:nowrap}
.nav a.active{color:var(--teal)}
.nav a.active::after{content:"";position:absolute;left:0;right:0;top:26px;height:3px;background:var(--teal)}
.icon-search{left:903px;top:36px;width:32px;height:32px;border:2px solid var(--navy);border-radius:50%}
.icon-cart{left:966px;top:38px}
.cart-count{left:980px;top:30px;width:16px;height:16px;border-radius:50%;border:1px solid var(--navy);font-size:10px;text-align:center;line-height:14px;background:var(--white)}
.lang{left:1028px;top:43px;font-size:14px;font-weight:700}

/* hero */
.hero{height:593px;background:
  radial-gradient(ellipse 260px 300px at 840px 200px,#c89878 0%,rgba(200,152,120,0) 70%),
  radial-gradient(ellipse 380px 260px at 900px 480px,#3f5c88 0%,rgba(63,92,136,0) 75%),
  radial-gradient(ellipse 300px 160px at 380px 520px,#eef0f2 0%,rgba(238,240,242,0) 70%),
  linear-gradient(100deg,#d6d2cc 0%,#e0a466 24%,#d78a42 42%,#9a6a48 58%,#4f6488 74%,#3b5078 100%)}
.hero-title{left:112px;top:180px;font-size:74px;color:var(--white);font-weight:600;letter-spacing:3px;text-shadow:0 2px 6px rgba(0,0,0,.15)}
.hero-sub{left:112px;top:293px;font-size:14px;color:var(--white);font-weight:700}
.btn-ghost{background:transparent;color:var(--navy-dark);border:2px solid var(--navy-dark)}
.slider-arrow{position:absolute;top:275px;width:42px;height:42px;border-radius:50%;background:var(--white);display:flex;align-items:center;justify-content:center}

/* who we are */
.about{height:565px}
.heading{font-size:38px;color:var(--ink)}
.lead{font-size:14px;font-weight:700;line-height:31px;color:var(--ink)}
.body-copy{font-size:14px;line-height:34px;color:var(--text);text-align:justify}

/* course sales */
.courses{height:749px;background:var(--soft)}
.center{left:0;right:0;text-align:center}
.tabs a{position:absolute;top:262px;font-size:13px;font-weight:700;color:var(--ink);transform:translateX(-50%);white-space:nowrap;text-decoration:none}
.tabs a.active::after{content:"";position:absolute;left:-12px;right:-12px;top:24px;height:3px;background:var(--navy)}
.course-card{position:absolute;top:345px;width:237px;height:319px;background:var(--white);border:1px solid var(--line);text-align:center}
.course-card.raised{box-shadow:0 6px 18px rgba(0,0,0,.15);height:334px;top:342px}
.course-img{height:164px;margin:4px 4px 0}
.badge{position:absolute;left:10px;top:10px;width:62px;height:15px;background:var(--sale);color:var(--white);font-size:8px;font-weight:900;line-height:15px}
.course-title{margin-top:20px;font-size:14px;font-weight:700}
.course-desc{margin-top:8px;font-size:13px;line-height:24px;color:var(--text)}
.price{margin-top:12px;font-size:22px;color:var(--teal);font-weight:700}
.price s{font-size:14px;margin-right:12px;color:var(--teal)}

/* certifications */
.certs{height:578px}
.tick-list{list-style:none}
.tick-list li{display:flex;align-items:center;gap:22px;font-size:15px;color:var(--text);height:39.5px}

/* subscription */
.subscription{height:517px;background:linear-gradient(180deg,#f2f5f9,#e6ebf2)}
.device{left:101px;top:138px;width:472px;height:236px;border-radius:10px;background:
  radial-gradient(ellipse 150px 90px at 280px 110px,#eef0f3 0%,rgba(238,240,243,0) 80%),
  linear-gradient(160deg,#22262e 0%,#545b66 30%,#c8ccd3 62%,#9aa1ab 100%)}

/* blog */
.blog{height:670px}
.blog-card{position:absolute;top:193px;width:317px;height:428px;background:var(--white);border:1px solid var(--line);box-shadow:0 2px 6px rgba(0,0,0,.05)}
.blog-img{height:211px;margin:2px 2px 0}
.blog-body{padding:20px 22px}
.blog-title{font-size:13px;font-weight:700;line-height:27px;text-transform:uppercase}
.blog-list{list-style:none;margin-top:10px}
.blog-list li{display:flex;align-items:center;gap:12px;font-size:12px;color:var(--text);height:27.5px}
.blog-link{display:inline-block;margin-top:10px;font-size:12px;font-weight:700;color:var(--teal);text-decoration:underline}

/* quote */
.quote{height:749px}
.quote-photo{left:556px;top:70px;width:510px;height:582px;background:
  radial-gradient(ellipse 140px 180px at 320px 260px,#d8b89c 0%,rgba(216,184,156,0) 75%),
  radial-gradient(ellipse 200px 140px at 330px 470px,#4d7db8 0%,rgba(77,125,184,0) 75%),
  linear-gradient(120deg,#e3ead8 0%,#f4f1ea 40%,#e9e6df 70%,#d6dade 100%)}
.quote-box{left:189px;top:125px;width:483px;height:409px;background:var(--teal)}
.quote-title{left:52px;top:58px;font-size:32px;color:var(--white)}
.field{position:absolute;height:41px;background:var(--white);border-radius:2px;font-size:12px;color:var(--muted);padding-left:14px;line-height:41px}
.submit{left:53px;top:294px;width:127px;height:40px;background:var(--navy);font-size:14px}
.call-box{left:336px;top:534px;width:336px;height:118px;background:var(--navy);color:var(--white)}
.call-label{left:109px;top:26px;font-size:18px;font-weight:700}
.call-number{left:109px;top:56px;font-size:31px;font-weight:700}

/* footer */
.site-footer{height:199px;background:var(--soft)}
.social{position:absolute;top:31px;width:36px;height:36px;border-radius:50%;border:2px solid var(--navy);display:flex;align-items:center;justify-content:center}
.footer-nav a{position:absolute;top:96px;font-size:14px;font-weight:700;color:var(--ink);text-decoration:none;transform:translateX(-50%);white-space:nowrap}
.copyright{top:147px;font-size:12px;color:var(--text)}
</style>
</head>
<body>
<svg width="0" height="0" style="position:absolute">
  <defs>
    <symbol id="arrow-circle" viewBox="0 0 14 14"><circle cx="7" cy="7" r="7" fill="currentColor"/><path d="M5.5 4 L8.5 7 L5.5 10" stroke="var(--navy)" stroke-width="1.8" fill="none"/></symbol>
    <symbol id="tick" viewBox="0 0 14 14"><circle cx="7" cy="7" r="6" fill="none" stroke="currentColor" stroke-width="1.5"/><path d="M4 7.2 L6.2 9.2 L10 5" stroke="currentColor" stroke-width="1.6" fill="none"/></symbol>
    <symbol id="cart" viewBox="0 0 24 24"><path d="M1 3h4l3 12h12l3-9H6.5" stroke="currentColor" stroke-width="2.4" fill="none" stroke-linejoin="round"/><circle cx="9" cy="20" r="2" fill="currentColor"/><circle cx="18" cy="20" r="2" fill="currentColor"/></symbol>
  </defs>
</svg>

<header class="section site-header">
  <div class="abs logo"><span class="logo-mark"></span><span class="logo-name">Velmont Data</span></div>
  <nav class="nav">
    <a class="active" href="#" style="left:344px">HOME</a>
    <a href="#" style="left:453px">LEARNING</a>
    <a href="#" style="left:560px">BLOG</a>
    <a href="#" style="left:659px">COURSE</a>
    <a href="#" style="left:796px">CERTIFICATIONS</a>
  </nav>
  <div class="abs icon-search"><svg width="28" height="28" viewBox="0 0 28 28"><circle cx="13" cy="13" r="5" stroke="var(--navy)" stroke-width="2" fill="none"/><path d="M16.5 16.5 L20 20" stroke="var(--navy)" stroke-width="2"/></svg></div>
  <svg class="abs icon-cart" width="24" height="24" style="color:var(--navy)"><use href="#cart"/></svg>
  <div class="abs cart-count">0</div>
  <div class="abs lang">ENG <svg width="10" height="8" viewBox="0 0 10 8"><path d="M1 2 L5 6 L9 2Z" fill="var(--ink)"/></svg></div>
</header>

<section class="section hero" role="img" aria-label="Photo of a smiling young woman in a denim shirt studying at a laptop">
  <h1 class="abs hero-title display">Velmont Data</h1>
  <p class="abs hero-sub">Lorem ipsum dolor sit amet, consectetur adipiscing elit, sed do eiusmod tempor incididunt</p>
  <a class="btn" style="left:114px;top:347px;width:191px;height:50px">Browse Courses <svg class="arrow" style="color:#fff"><use href="#arrow-circle"/></svg></a>
  <a class="btn btn-ghost" style="left:327px;top:347px;width:192px;height:50px">Discussion Forum <svg class="arrow" style="color:var(--navy-dark)"><use href="#arrow-circle"/></svg></a>
  <span class="slider-arrow" style="left:34px"><svg width="14" height="18" viewBox="0 0 14 18"><path d="M10 2 L3 9 L10 16" stroke="#111" stroke-width="3" fill="none"/></svg></span>
  <span class="slider-arrow" style="left:1122px"><svg width="14" height="18" viewBox="0 0 14 18"><path d="M4 2 L11 9 L4 16" stroke="#111" stroke-width="3" fill="none"/></svg></span>
</section>

<section class="section about">
  <div class="photo" style="left:112px;top:117px;width:462px;height:332px;background:radial-gradient(ellipse 90px 110px at 370px 130px,#3a3f48 0%,rgba(58,63,72,0) 80%),radial-gradient(ellipse 110px 80px at 120px 110px,#8f9aa6 0%,rgba(143,154,166,0) 80%),linear-gradient(180deg,#eef1f3 0%,#e4e8eb 62%,#c8ad8c 80%,#a88a68 100%)" role="img" aria-label="Photo of a man with a headset working at a desktop computer"></div>
  <h2 class="abs heading display" style="left:650px;top:100px">Who We Are</h2>
  <p class="abs lead" style="left:650px;top:157px;width:438px">Duis aute irure dolor in reprehenderit in voluptate velit esse cillum dolore eu fugiat nulla pariatur.</p>
  <p class="abs body-copy" style="left:650px;top:228px;width:414px">Sed ut perspiciatis unde omnis iste natus error sit voluptatem accusantium doloremque laudantium, totam rem aperiam, eaque ipsa quae ab illo inventore veritatis et quasi architecto beatae vitae dicta sunt explicabo. Nemo enim ipsam voluptatem quia voluptas sit aspernatur.</p>
  <a class="btn" style="left:650px;top:418px;width:152px;height:50px">Read More <svg class="arrow" style="color:#fff"><use href="#arrow-circle"/></svg></a>
</section>

<section class="section courses">
  <h2 class="abs center heading display" style="top:75px">Course Sales</h2>
  <p class="abs center" style="top:144px;font-size:14px;line-height:35px;color:var(--text)">At vero eos et accusamus et iusto odio dignissimos ducimus qui blanditiis praesentium voluptatum<br>deleniti atque corrupti quos dolores et quas molestias excepturi sint.</p>
  <nav class="tabs">
    <a class="active" href="#" style="left:246px">ALL</a>
    <a href="#" style="left:356px">BUSINESS</a>
    <a href="#" style="left:508px">IT &amp; SOFTWARE</a>
    <a href="#" style="left:725px">PERSONAL DEVELOPEMENT</a>
    <a href="#" style="left:934px">MARKETTING</a>
  </nav>
  <article class="course-card" style="left:112px">
    <div class="course-img" style="background:radial-gradient(ellipse 70px 60px at 150px 50px,#4a3a30 0%,rgba(74,58,48,0) 80%),linear-gradient(180deg,#e8e4dc 0%,#d9d2c6 55%,#b4a58f 100%)" role="img" aria-label="Photo of a student writing in a notebook"></div>
    <h3 class="course-title">COURSE TITLE</h3>
    <p class="course-desc">Et harum quidem rerum facilis et<br>expedita distinctio.</p>
    <p class="price"><s>$25.00</s>$15.00</p>
  </article>
  <article class="course-card" style="left:358px">
    <div class="course-img" style="background:radial-gradient(ellipse 60px 80px at 90px 80px,#23283a 0%,rgba(35,40,58,0) 85%),linear-gradient(135deg,#f1efeb 0%,#dcd9d3 50%,#bfc2c8 100%)" role="img" aria-label="Photo of a woman taking notes beside a laptop"></div>
    <span class="badge">BEST SELLER</span>
    <h3 class="course-title">COURSE TITLE</h3>
    <p class="course-desc">Et harum quidem rerum facilis et<br>expedita distinctio.</p>
    <p class="price"><s>$25.00</s>$15.00</p>
  </article>
  <article class="course-card raised" style="left:605px">
    <div class="course-img" style="background:radial-gradient(ellipse 70px 80px at 170px 90px,#5f7fa4 0%,rgba(95,127,164,0) 80%),linear-gradient(135deg,#5a4a3e 0%,#7a634f 45%,#4e5e72 100%)" role="img" aria-label="Photo of two people working on laptops at a wooden table"></div>
    <h3 class="course-title">COURSE TITLE</h3>
    <p class="course-desc">Et harum quidem rerum facilis et<br>expedita distinctio.</p>
    <p class="price"><s>$25.00</s>$15.00</p>
  </article>
  <a class="btn" style="left:666px;top:657px;width:112px;height:37px;font-size:10px;gap:6px">Add to cart <svg width="11" height="11" style="color:#fff"><use href="#cart"/></svg></a>
  <article class="course-card" style="left:851px">
    <div class="course-img" style="background:radial-gradient(ellipse 60px 75px at 100px 80px,#c7a892 0%,rgba(199,168,146,0) 80%),linear-gradient(135deg,#e2ddd4 0%,#cfc6b8 55%,#8c7a66 100%)" role="img" aria-label="Photo of a woman with headphones at a laptop"></div>
    <span class="badge">BEST SELLER</span>
    <h3 class="course-title">COURSE TITLE</h3>
    <p class="course-desc">Et harum quidem rerum facilis et<br>expedita distinctio.</p>
    <p class="price"><s>$25.00</s>$15.00</p>
  </article>
</section>

<section class="section certs">
  <h2 class="abs heading display" style="left:112px;top:120px;font-size:39px">National Certifications</h2>
  <ul class="abs tick-list" style="left:112px;top:181px">
    <li><svg width="14" height="14" style="color:var(--navy)"><use href="#tick"/></svg>Duis aute irure dolor in repre&nbsp; dolor in repre</li>
    <li><svg width="14" height="14" style="color:var(--navy)"><use href="#tick"/></svg>Duis aute irure dolor in repre&nbsp; dolor in repre</li>
    <li><svg width="14" height="14" style="color:var(--navy)"><use href="#tick"/></svg>Duis aute irure dolor in repre&nbsp; dolor in repre</li>
    <li><svg width="14" height="14" style="color:var(--navy)"><use href="#tick"/></svg>Duis aute irure dolor in repre&nbsp; dolor in repre</li>
    <li><svg width="14" height="14" style="color:var(--navy)"><use href="#tick"/></svg>Duis aute irure dolor in repre&nbsp; dolor in repre</li>
  </ul>
  <a class="btn" style="left:112px;top:404px;width:154px;height:51px">View Pricing <svg class="arrow" style="color:#fff"><use href="#arrow-circle"/></svg></a>
  <div class="photo" style="left:626px;top:125px;width:462px;height:332px;background:radial-gradient(ellipse 110px 130px at 230px 140px,#c49a7e 0%,rgba(196,154,126,0) 75%),radial-gradient(ellipse 160px 70px at 330px 290px,#e8e2d8 0%,rgba(232,226,216,0) 80%),linear-gradient(135deg,#2e2926 0%,#5a4c40 40%,#8a7866 70%,#cfc3b2 100%)" role="img" aria-label="Photo of a young woman with headphones writing notes at a laptop"></div>
</section>

<section class="section subscription">
  <div class="abs device" role="img" aria-label="Illustration of a laptop and tablet showing an online lesson"></div>
  <h2 class="abs heading display" style="left:615px;top:70px;font-size:35px">Programming Subscription</h2>
  <p class="abs lead" style="left:615px;top:124px;width:438px">Duis aute irure dolor in reprehenderit in voluptate velit esse cillum dolore eu fugiat nulla pariatur.</p>
  <p class="abs body-copy" style="left:615px;top:198px;width:414px">Sed ut perspiciatis unde omnis iste natus error sit voluptatem accusantium doloremque laudantium, totam rem aperiam, eaque ipsa quae ab illo inventore veritatis et quasi architecto beatae vitae dicta sunt explicabo. Nemo enim ipsam voluptatem quia voluptas sit aspernatur.</p>
  <a class="btn" style="left:615px;top:389px;width:154px;height:50px">Read More <svg class="arrow" style="color:#fff"><use href="#arrow-circle"/></svg></a>
</section>

<section class="section blog">
  <h2 class="abs center heading display" style="top:90px">Latest Blog</h2>
  <article class="blog-card" style="left:112px">
    <div class="blog-img" style="background:radial-gradient(ellipse 80px 90px at 190px 90px,#2f4a78 0%,rgba(47,74,120,0) 80%),radial-gradient(ellipse 140px 50px at 150px 190px,#ece8e0 0%,rgba(236,232,224,0) 85%),linear-gradient(135deg,#34502e 0%,#6a6a48 45%,#9a8a70 100%)" role="img" aria-label="Photo of a young man reading at a desk with a laptop"></div>
    <div class="blog-body">
      <h3 class="blog-title">Sed ut perspiciatis unde omnis iste natus error sit voluptatem</h3>
      <ul class="blog-list">
        <li><svg width="12" height="12" style="color:var(--teal)"><use href="#tick"/></svg>Lorem ipsum dolor sit amet, consectetur</li>
        <li><svg width="12" height="12" style="color:var(--teal)"><use href="#tick"/></svg>Lorem ipsum dolor sit amet, consectetur</li>
        <li><svg width="12" height="12" style="color:var(--teal)"><use href="#tick"/></svg>Lorem ipsum dolor sit amet, consectetur</li>
      </ul>
      <a class="blog-link" href="#">BROWSE ALL COURSES</a>
    </div>
  </article>
  <article class="blog-card" style="left:442px">
    <div class="blog-img" style="background:radial-gradient(ellipse 70px 100px at 150px 110px,#8fa8c8 0%,rgba(143,168,200,0) 80%),radial-gradient(ellipse 50px 50px at 150px 50px,#b8866a 0%,rgba(184,134,106,0) 80%),linear-gradient(180deg,#efede9 0%,#e2ded7 60%,#c9c2b6 100%)" role="img" aria-label="Photo of a woman with headphones writing beside a laptop"></div>
    <div class="blog-body">
      <h3 class="blog-title">Sed ut perspiciatis unde omnis iste natus error sit voluptatem</h3>
      <ul class="blog-list">
        <li><svg width="12" height="12" style="color:var(--teal)"><use href="#tick"/></svg>Lorem ipsum dolor sit amet, consectetur</li>
        <li><svg width="12" height="12" style="color:var(--teal)"><use href="#tick"/></svg>Lorem ipsum dolor sit amet, consectetur</li>
        <li><svg width="12" height="12" style="color:var(--teal)"><use href="#tick"/></svg>Lorem ipsum dolor sit amet, consectetur</li>
      </ul>
      <a class="blog-link" href="#">BROWSE ALL COURSES</a>
    </div>
  </article>
  <article class="blog-card" style="left:771px">
    <div class="blog-img" style="background:radial-gradient(ellipse 60px 90px at 200px 90px,#4a3a32 0%,rgba(74,58,50,0) 80%),radial-gradient(ellipse 80px 50px at 80px 150px,#6e7178 0%,rgba(110,113,120,0) 80%),linear-gradient(180deg,#e4e0d8 0%,#d3ccc0 55%,#a69a88 100%)" role="img" aria-label="Photo of a woman taking notes with a laptop on a table"></div>
    <div class="blog-body">
      <h3 class="blog-title">Sed ut perspiciatis unde omnis iste natus error sit voluptatem</h3>
      <ul class="blog-list">
        <li><svg width="12" height="12" style="color:var(--teal)"><use href="#tick"/></svg>Lorem ipsum dolor sit amet, consectetur</li>
        <li><svg width="12" height="12" style="color:var(--teal)"><use href="#tick"/></svg>Lorem ipsum dolor sit amet, consectetur</li>
        <li><svg width="12" height="12" style="color:var(--teal)"><use href="#tick"/></svg>Lorem ipsum dolor sit amet, consectetur</li>
      </ul>
      <a class="blog-link" href="#">BROWSE ALL COURSES</a>
    </div>
  </article>
</section>

<section class="section quote">
  <div class="abs quote-photo" role="img" aria-label="Photo of a woman with glasses and headphones writing at a desk"></div>
  <div class="abs quote-box">
    <h2 class="abs quote-title display">Get A Free Quote</h2>
    <div class="field" style="left:53px;top:108px;width:178px">First Name</div>
    <div class="field" style="left:244px;top:108px;width:178px">Last Name</div>
    <div class="field" style="left:53px;top:160px;width:365px">Email Address</div>
    <div class="field" style="left:53px;top:215px;width:365px">Phone No</div>
    <a class="btn submit">Submit Now</a>
  </div>
  <div class="abs call-box">
    <svg class="abs" style="left:24px;top:30px" width="58" height="58" viewBox="0 0 58 58" fill="none" stroke="#fff" stroke-width="2.2"><path d="M14 8 L22 18 L17 24 Q22 34 33 40 L39 35 L49 43 L43 51 Q22 48 8 17 Z"/><path d="M33 10 Q46 12 48 25"/><path d="M32 17 Q40 18 41 26"/></svg>
    <p class="abs call-label">Get a Free Quote Today</p>
    <p class="abs call-number">888 555 0142</p>
  </div>
</section>

<footer class="section site-footer">
  <span class="social" style="left:518px" aria-label="Email"><svg width="16" height="12" viewBox="0 0 16 12" fill="none" stroke="var(--navy)" stroke-width="1.6"><rect x="1" y="1" width="14" height="10" rx="1"/><path d="M1 1 L8 7 L15 1"/></svg></span>
  <span class="social" style="left:560px" aria-label="Chat"><svg width="16" height="15" viewBox="0 0 16 15" fill="none" stroke="var(--navy)" stroke-width="1.6"><path d="M2 1h12a1 1 0 0 1 1 1v7a1 1 0 0 1-1 1H7l-4 3v-3H2a1 1 0 0 1-1-1V2a1 1 0 0 1 1-1z"/></svg></span>
  <span class="social" style="left:602px" aria-label="Share"><svg width="16" height="16" viewBox="0 0 16 16" fill="var(--navy)" stroke="var(--navy)" stroke-width="1.4"><circle cx="12" cy="3" r="2"/><circle cx="4" cy="8" r="2"/><circle cx="12" cy="13" r="2"/><path d="M12 3 L4 8 L12 13" fill="none"/></svg></span>
  <span class="social" style="left:644px" aria-label="Website"><svg width="16" height="16" viewBox="0 0 16 16" fill="none" stroke="var(--navy)" stroke-width="1.4"><circle cx="8" cy="8" r="7"/><ellipse cx="8" cy="8" rx="3" ry="7"/><path d="M1 8h14"/></svg></span>
  <nav class="footer-nav">
    <a href="#" style="left:354px">HOME</a>
    <a href="#" style="left:464px">LEARNING</a>
    <a href="#" style="left:571px">BLOG</a>
    <a href="#" style="left:668px">COURSE</a>
    <a href="#" style="left:806px">CERTIFICATIONS</a>
  </nav>
  <p class="abs center copyright">© 2020 Velmont Data. All Rights reserved</p>
</footer>
</body>
</html>
```